Science News Webpage Design

Quarry Lantern Works gGmbH is a non-profit organisation developing apps for scientists. Our main project is a scientific platform you can visit at quarrylantern.net.

The QLW platform consists of multiple modules. We are now considering to spin out one of the modules (Tides & Notes) and create a separate web application with focus on latest science news that enables scientists to easily contribute by writing their own articles and commentaries.

For this news website, we need someone to design the homepage and three other templates.

We prepared a set of files consisting of a more detailed brief and also a couple of wire-frames.

Please check these files and get in touch with us in case you have questions or in case something is unclear.
Updates

Hello everyone,

Just a short note. Although I have indicated in the brief that this project is a spin-out from another platform, you shouldn't feel restricted to design and color combinations of that other site. We are really trying to make something new here, and the design can be completely different.

I also attached a new file. The working title of the project is "wonder unwrapped". Although we haven't decided on the final name, you can use this png as logo.

Cheers,
Toma

Updated home page wireframe to include all links in the menu (since there are more links than originally depicted and this obviously influences design).

Industry/Entity Type

Non-Profit

```html
<!DOCTYPE html>
<html lang="en">
<head>
<meta charset="utf-8">
<title>Quarry Lantern Works – Tides &amp; Notes</title>
<link href="https://fonts.googleapis.com/css2?family=Arimo:wght@400;700&display=swap" rel="stylesheet">
<style>
:root{
  --ad-band:#d5d5d5;--ad-frame:#6b6b6b;--ad-text:#e8402f;
  --header:#575757;--white:#fff;--text:#555;--text-dark:#444;
  --green:#8ccf2a;--green-dark:#5e9a14;--green-soft:#c8ec84;
  --teal:#2e8fa0;--teal-light:#4fb3c6;--teal-dark:#23808f;
  --red:#d93a2b;--salmon:#f5726a;--pill:#b8b8b8;--panel:#efefef;--line:#e3e3e3;
}
*{margin:0;padding:0;box-sizing:border-box}
html,body{width:1200px;height:1000px;overflow:hidden;background:var(--white)}
body{position:relative;font-family:"Arimo",Arial,sans-serif;color:var(--text)}
.abs{position:absolute}
.ad-band{left:0;top:0;width:1200px;height:124px;background:var(--ad-band)}
.ad{border:4px solid var(--ad-frame);display:flex;align-items:center;justify-content:center;text-align:center;color:var(--ad-text);font-size:12px;font-weight:700;line-height:14px}
.ad-leader{left:236px;top:18px;width:728px;height:90px}
.site-header{left:0;top:124px;width:1200px;height:134px;background:var(--header)}
.brand{left:123px;top:143px;display:flex;align-items:flex-start;gap:12px}
.brand-dot{width:26px;height:26px;border-radius:50%;background:var(--teal-light);margin-top:4px}
.brand-name{color:var(--white);font-weight:700;font-size:25px;line-height:26px}
.tagline{left:320px;top:178px;font-size:15px;color:var(--white)}
.tagline span{color:var(--green)}
.nav{left:135px;top:226px;font-size:15px;color:var(--white);white-space:nowrap}
.nav a{color:var(--white);text-decoration:none}
.nav .active{color:var(--green)}
.nav i{font-style:normal;margin:0 6px}
.btn{display:flex;align-items:center;justify-content:center;color:var(--white);font-weight:700;border-radius:3px}
.btn-red{background:var(--red)}
.btn-green{background:var(--green)}
.auth-in{left:920px;top:166px;width:60px;height:26px;font-size:12px}
.auth-or{left:988px;top:173px;font-size:10px;font-weight:700;color:var(--white)}
.auth-up{left:1012px;top:166px;width:63px;height:26px;font-size:12px}
.follow{left:967px;top:206px;font-size:11px;color:var(--white)}
.social{top:221px;width:21px;height:21px;background:#8a9fb3;border-radius:2px}
.tab-latest{left:0;top:284px;z-index:2}
.pill{background:var(--pill);color:var(--white);font-size:16px;border-radius:6px;display:flex;align-items:center;justify-content:center}
.photo{background:linear-gradient(160deg,#9a9a9a,#3f3f3f)}
.lead-headline{left:134px;top:480px;width:300px;font-size:20px;line-height:20px}
.meta{font-weight:700;font-size:15px;line-height:16px;color:var(--text-dark)}
.meta b{color:var(--teal-light);font-weight:400}
.lead-body{left:135px;top:601px;width:288px;font-size:15px;line-height:15.5px}
.read{color:var(--teal);text-decoration:none;border-bottom:1px solid var(--teal);font-size:15px;line-height:16px}
.list{left:445px;top:310px;width:316px;height:410px;background:var(--panel);overflow:hidden}
.item{position:absolute;left:0;width:296px;height:104px;background:var(--white)}
.item .thumb{position:absolute;left:12px;top:8px;width:78px;height:78px;background:var(--green-soft)}
.item p{position:absolute;left:97px;top:8px;width:195px;font-size:13.5px;line-height:14px}
.item .read{position:absolute;left:215px;top:68px;font-size:14px}
.scroll{right:0;top:0;width:20px;height:410px;background:#e2e2e2}
.search-input{left:821px;top:292px;width:214px;height:32px;background:var(--white);border-radius:2px 0 0 2px;font-size:16px;color:#b5b5b5;padding:7px 10px}
.search-btn{left:1036px;top:292px;width:40px;height:32px;background:var(--red);border-radius:0 2px 2px 0}
.cta-panel{left:773px;top:333px;width:300px;height:137px;background:var(--panel)}
.cta-up{left:861px;top:344px;width:135px;height:38px;font-size:18px;font-weight:400;border-radius:6px}
.cta-note{left:773px;top:389px;width:310px;text-align:center;font-size:15px}
.cta-more{left:861px;top:414px;width:135px;height:38px;font-size:16px;font-weight:400;border-radius:6px}
.ad-box{left:773px;top:470px;width:300px;height:250px;background:var(--panel)}
.rule{left:125px;top:742px;width:955px;height:1px;background:var(--line)}
.vrule{top:765px;width:1px;height:235px;background:var(--line)}
.sec-title{top:769px;font-size:20px;text-transform:uppercase}
.sec-headline{top:972px;width:300px;font-size:20px;line-height:20px}
.pop{left:779px;width:300px;height:85px}
.pop .thumb{position:absolute;left:0;top:0;width:78px;height:78px;background:var(--salmon)}
.pop p{position:absolute;left:85px;top:0;width:210px;font-size:13.5px;line-height:14px}
.pop .meta{position:absolute;right:5px;top:46px;font-size:13.5px}
.pop .read{position:absolute;right:5px;top:62px;font-size:14px}
</style>
</head>
<body>
<div class="abs ad-band"></div>
<div class="abs ad ad-leader">728 X 90<br>ADVERTISEMENT</div>

<header class="abs site-header"></header>
<div class="abs brand"><span class="brand-dot"></span><div class="brand-name">Quarry Lantern<br>Works</div></div>
<div class="abs tagline">wonder <span>unwrapped.</span></div>
<nav class="abs nav"><a class="active">LATEST</a><i>/</i><a>BIOLOGY</a><i>/</i><a>CHEMISTRY</a><i>/</i><a>PHYSICS</a><i>/</i><a>COMPUTATION</a><i>/</i><a>TECHNOLOGY</a><i>/</i><a>HEALTH</a><i>/</i><a>QUESTIONS?</a></nav>
<div class="abs btn btn-red auth-in">Sign in</div>
<div class="abs auth-or">OR</div>
<div class="abs btn btn-red auth-up">Sign up</div>
<div class="abs follow">Follow us</div>
<span class="abs social" style="left:966px"></span>
<span class="abs social" style="left:996px"></span>
<span class="abs social" style="left:1025px"></span>
<span class="abs social" style="left:1054px"></span>

<div class="abs photo" style="left:134px;top:310px;width:302px;height:160px" role="img" aria-label="Photo of a hand writing notes beside a calculator"></div>
<svg class="abs tab-latest" width="352" height="50" viewBox="0 0 352 50">
  <rect x="0" y="0" width="15" height="50" fill="#5e9a14"/>
  <polygon points="15,0 340,0 351,25 340,50 15,50" fill="#8ccf2a"/>
  <text x="135" y="31" fill="#fff" font-family="Arimo, Arial, sans-serif" font-size="19">LATEST</text>
</svg>
<div class="abs pill" style="left:691px;top:277px;width:70px;height:28px">See all</div>

<h2 class="abs lead-headline" style="font-weight:400">Lorem ipsum dolor sit amet, consectetur adipiscing elit. In tincidunt erat scelerisque.</h2>
<div class="abs meta" style="left:135px;top:556px">Generic engineering <b>|</b> Article<br>by R. Halden</div>
<p class="abs lead-body">Lorem ipsum dolor sit amet, consectetur adipiscing elit. Nullam mollis aliquam semper. In tincidunt erat scelerisque ipsum vulputate dictum. Mauris in purus eros. Nunc condimentum, dui et pharetra...</p>
<a class="abs read" style="left:354px;top:700px">Read more</a>

<div class="abs list">
  <div class="item" style="top:-30px;height:92px"><span class="thumb"></span><p>Lorem ipsum dolor sit amet, consectetur adipiscing elit. In tincidunt erat scelerisque.</p><a class="read">Read more</a></div>
  <div class="item" style="top:70px"><span class="thumb"></span><p>Lorem ipsum dolor sit amet, consectetur adipiscing elit. In tincidunt erat scelerisque.</p><a class="read">Read more</a></div>
  <div class="item" style="top:176px"><span class="thumb"></span><p>Lorem ipsum dolor sit amet, consectetur adipiscing elit. In tincidunt erat scelerisque.</p><a class="read">Read more</a></div>
  <div class="item" style="top:282px"><span class="thumb"></span><p>Lorem ipsum dolor sit amet, consectetur adipiscing elit. In tincidunt erat scelerisque.</p><a class="read">Read more</a></div>
  <div class="item" style="top:388px"><span class="thumb"></span><p>Lorem ipsum dolor sit amet, consectetur adipiscing elit. In tincidunt erat scelerisque.</p></div>
  <svg class="abs scroll" viewBox="0 0 20 410" width="20" height="410">
    <rect x="0" y="0" width="20" height="18" fill="#bdbdbd"/><polygon points="6,13 14,13 10,6" fill="#fff"/>
    <rect x="0" y="392" width="20" height="18" fill="#bdbdbd"/><polygon points="6,397 14,397 10,404" fill="#fff"/>
    <rect x="3" y="71" width="15" height="52" rx="3" fill="#4fb3c6"/>
  </svg>
</div>

<svg class="abs" style="left:805px;top:284px" width="395" height="50" viewBox="0 0 395 50">
  <polygon points="0,0 380,0 380,50 0,50 12,25" fill="#4fb3c6"/>
  <rect x="380" y="0" width="15" height="50" fill="#23808f"/>
</svg>
<div class="abs search-input">Search</div>
<svg class="abs search-btn" viewBox="0 0 40 32" width="40" height="32"><circle cx="21" cy="14" r="6" fill="none" stroke="#fff" stroke-width="3"/><line x1="17" y1="18" x2="12" y2="24" stroke="#fff" stroke-width="3.5" stroke-linecap="round"/></svg>

<div class="abs cta-panel"></div>
<div class="abs btn btn-red cta-up">Sign up</div>
<div class="abs cta-note">to upload articles, bookmark, comment...</div>
<div class="abs btn btn-green cta-more">Find out more</div>
<div class="abs ad ad-box">300 X 250<br>ADVERTISEMENT</div>

<div class="abs rule"></div>
<div class="abs vrule" style="left:442px"></div>
<div class="abs vrule" style="left:765px"></div>

<h3 class="abs sec-title" style="left:135px;color:var(--teal);font-weight:400">Biology</h3>
<div class="abs pill" style="left:359px;top:762px;width:70px;height:29px">See all</div>
<div class="abs photo" style="left:136px;top:799px;width:292px;height:161px;background:linear-gradient(150deg,#8d8d8d,#4a4a4a)" role="img" aria-label="Microscope image of a roundworm"></div>
<h4 class="abs sec-headline" style="left:136px;font-weight:400">Lorem ipsum dolor sit amet, consectetur adipiscing elit. In</h4>

<h3 class="abs sec-title" style="left:457px;color:var(--green);font-weight:400">Chemistry</h3>
<div class="abs pill" style="left:679px;top:762px;width:70px;height:29px">See all</div>
<div class="abs" style="left:490px;top:799px;width:220px;height:161px;background:radial-gradient(circle at 45% 45%,#c9d1cf,#eef0ef 75%,#fff)" role="img" aria-label="Illustration of a petri dish culture with molecular diagrams"></div>
<h4 class="abs sec-headline" style="left:456px;font-weight:400">Lorem ipsum dolor sit amet, consectetur adipiscing elit. In</h4>

<h3 class="abs sec-title" style="left:778px;color:#e8473a;font-weight:400">Most popular</h3>
<div class="abs pill" style="left:1009px;top:762px;width:70px;height:29px">See all</div>
<div class="abs pop" style="top:800px"><span class="thumb"></span><p>Lorem ipsum dolor sit amet, consectetur adipiscing elit. In tincidunt erat scelerisque.</p><div class="meta">Generic engineering <b>|</b> Article</div><a class="read">Read more</a></div>
<div class="abs pop" style="top:906px"><span class="thumb"></span><p>Lorem ipsum dolor sit amet, consectetur adipiscing elit. In tincidunt erat scelerisque.</p><div class="meta">Generic engineering <b>|</b> Article</div><a class="read">Read more</a></div>
</body>
</html>
```